Card Design to Advertise New Business

I am looking to have a card designed so that I can pass it out to help promote my business. I have never done this before so I honestly do not know where to start with any ideas. I am providing my website address to help. I provide math tutoring, test prep, and schooling options.

I am looking for a card bigger than a business card but smaller than a flyer. Something front and back that I can pass out.

Business Information
Phone: 470-555-0192
Website: www.kelvanostudyhall.example
Address: 418 Brackenfield Rd Ste 340 Marietta GA 30072
Email: kelvanoservices@kelvanomail.example

Services:
Math Tutoring
NEQ & BOW Test Prep
Group and Private Sessions
Fully Accredited Private School

Target Market(s)

Middle and High School Students

Industry/Entity Type

Education

Requirements
Must have
• Information from my website

```html
<!DOCTYPE html>
<html lang="en">
<head>
<meta charset="utf-8">
<title>Kelvano Study Hall – Promo Card</title>
<link href="https://fonts.googleapis.com/css2?family=Noto+Serif:wght@400;700&display=swap" rel="stylesheet">
<style>
  :root {
    --stage: #fbf2ec;
    --paper: #ffffff;
    --green: #00c800;
    --ink: #111111;
    --star: #d42a12;
  }
  * { margin: 0; padding: 0; box-sizing: border-box; }
  html, body { width: 1200px; height: 811px; overflow: hidden; }
  body {
    background: var(--stage);
    font-family: "Noto Serif", Georgia, serif;
    color: var(--ink);
    position: relative;
  }
  .card {
    position: absolute;
    top: 78px;
    width: 429px;
    height: 644px;
    background: var(--paper);
    overflow: hidden;
  }
  .card--front { left: 116px; }
  .card--back { left: 654px; }
  .card__shapes { position: absolute; inset: 0; width: 100%; height: 100%; }
  .card__shapes circle { fill: var(--green); }

  .brand {
    position: absolute;
    display: flex;
    align-items: center;
    white-space: nowrap;
  }
  .brand__dot {
    border-radius: 50%;
    background: var(--green);
    flex: none;
  }
  .brand__name { font-weight: 700; color: var(--ink); }

  .brand--front { left: 55px; top: 235px; gap: 10px; }
  .brand--front .brand__dot { width: 116px; height: 116px; }
  .brand--front .brand__name { font-size: 20px; }

  .brand--back { left: 32px; top: 43px; width: 100px; flex-direction: column; gap: 6px; }
  .brand--back .brand__dot { width: 51px; height: 51px; }
  .brand--back .brand__name { font-size: 10px; }

  .contact {
    position: absolute;
    left: 0; right: 0; top: 175px;
    text-align: center;
    font-size: 10.5px;
    font-weight: 700;
    font-style: normal;
    line-height: 16px;
  }
  .services {
    position: absolute;
    left: 0; right: 0; top: 280px;
    list-style: none;
    text-align: center;
  }
  .services__item {
    font-size: 14.5px;
    font-weight: 700;
    line-height: 22px;
  }
  .services__star {
    color: var(--star);
    font-size: 10px;
    line-height: 10.5px;
  }
  .website {
    position: absolute;
    left: 0; right: 0; top: 487px;
    text-align: center;
    font-size: 11px;
    font-weight: 700;
  }
</style>
</head>
<body>
  <section class="card card--front">
    <svg class="card__shapes" viewBox="0 0 429 644" aria-hidden="true">
      <circle cx="214" cy="-96" r="177"/>
      <circle cx="214" cy="722" r="176"/>
      <circle cx="149" cy="128" r="20.5"/>
      <circle cx="266" cy="466" r="12"/>
    </svg>
    <div class="brand brand--front">
      <span class="brand__dot"></span>
      <span class="brand__name">Kelvano Study Hall</span>
    </div>
  </section>

  <section class="card card--back">
    <svg class="card__shapes" viewBox="0 0 429 644" aria-hidden="true">
      <circle cx="456" cy="-64" r="179"/>
      <circle cx="214" cy="722" r="176"/>
      <circle cx="255" cy="52" r="14"/>
    </svg>
    <div class="brand brand--back">
      <span class="brand__dot"></span>
      <span class="brand__name">Kelvano Study Hall</span>
    </div>
    <address class="contact">
      <p>Phone: 470-555-0192</p>
      <p>Address: 418 Brackenfield Rd Ste 340 Marietta GA 30072</p>
      <p>Email: kelvanoservices@kelvanomail.example</p>
    </address>
    <ul class="services">
      <li class="services__item">Math Tutoring</li>
      <li class="services__star">★</li>
      <li class="services__item">NEQ &amp; BOW Test Prep</li>
      <li class="services__star">★</li>
      <li class="services__item">Group and Private Sessions</li>
      <li class="services__star">★</li>
      <li class="services__item">Fully Accredited Private School</li>
    </ul>
    <p class="website">www.kelvanostudyhall.example</p>
  </section>
</body>
</html>
```